Professional website for psychological services

Create a professional, easy to navigate website using soothing coastal images and incorporate company logo in design. Website is for a small private clinic that provides psychological services and must be appealing to professional men and women. A website I really like is www.velmorlodge.example I would love something like similar.

Target Market(s)

Professional men and women seeking psychological services

Industry/Entity Type

Mental Health

Number of Pages Required

5+ page

Requirements
Must have
• The website must incorporate the logo provided. The name of the company/website is Brindle Oak Wellness Aftercare. Colors must compliment the logo, must be coastal and soothing yet very professional. I would like a website like www.velmorlodge.example
• Pages will be:Home, Services, FAQ and Contact Us. The images included of the building and office are for the contact us page. Under the tab Servies: Individual Psychotherapy, Family Therapy, EMDR I will provide specific content for each.
Nice to have
• I want the website to be easy to navigate and the font easy to read. The writing on the logo is very light and I'm open to changing it slightly if it will be better aesthetically.
Should not have
• Please no pictures of any swimsuits, alcoholic beverages, etc. This is a professional psychological clinic.

```html
<!DOCTYPE html>
<html lang="en">
<head>
<meta charset="utf-8">
<title>Brindle Oak Wellness Aftercare</title>
<link rel="stylesheet" href="https://fonts.googleapis.com/css2?family=Kaushan+Script&family=Roboto:wght@400;500;700&display=swap">
<style>
:root{
  --teal:#0c7b86;
  --teal-dark:#0a6e78;
  --cyan:#17b6cf;
  --sand:#e7d6c3;
  --orange:#de953f;
  --ink:#2b2b2b;
  --muted:#f3f3f3;
  --white:#ffffff;
  --line:#d6d6d6;
}
*{box-sizing:border-box;margin:0;padding:0}
html,body{width:1200px;height:3509px;overflow:hidden}
body{font-family:"Roboto",Arial,sans-serif;color:var(--ink);background:var(--white)}
.page{position:relative;width:1200px;height:3509px;overflow:hidden}
.abs{position:absolute}
.script{font-family:"Kaushan Script",cursive;font-weight:400}

/* brand */
.brand{position:absolute;display:flex;flex-direction:column;align-items:center;gap:10px;width:200px}
.brand-dot{width:34px;height:34px;border-radius:50%}
.brand-name{font-family:"Roboto",Arial,sans-serif;font-weight:400;text-align:center;line-height:1.15;white-space:nowrap}
.hero-brand{left:92px;top:42px}
.hero-brand .brand-dot{background:var(--teal)}
.hero-brand .brand-name{color:var(--teal);font-size:26px}
.footer-brand{left:90px;top:3200px}
.footer-brand .brand-dot{background:var(--white)}
.footer-brand .brand-name{color:var(--white);font-size:28px}

/* hero */
.hero-art{position:absolute;left:0;top:0}
.nav{position:absolute;left:362px;top:100px;display:flex;gap:19px}
.nav a{color:var(--white);text-decoration:none;font-size:16px;font-weight:700}
.hero-title{position:absolute;left:100px;top:262px;width:560px;text-align:center;color:var(--white);font-size:54px;line-height:66px;white-space:nowrap}
.btn{position:absolute;display:flex;align-items:center;justify-content:center;background:var(--cyan);color:var(--white);font-size:18px;font-weight:500;text-decoration:none;border:0}
.hero-btn{left:316px;top:491px;width:124px;height:49px;border:2px solid rgba(255,255,255,.55)}

/* about */
.about-frame{left:92px;top:880px;width:440px;height:380px;background:var(--orange);border-radius:48px;transform:rotate(-5deg)}
.about-photo{left:114px;top:944px;width:424px;height:262px;background:linear-gradient(135deg,#6d8a3c 0%,#5a4030 45%,#c9a07e 70%,#8aa456 100%);border-radius:6px;transform:rotate(-2deg)}
.about-title{left:592px;top:930px;font-size:50px;color:var(--teal)}
.about-text{left:592px;top:1018px;width:470px;font-size:18px;line-height:27px;color:#333}
.about-btn{left:592px;top:1158px;width:125px;height:47px}

/* services */
.services-title{left:0;top:1355px;width:1200px;text-align:center;font-size:50px;color:var(--teal)}
.service-card{position:absolute;top:1497px;width:244px;height:326px;background:var(--white);border:1px solid #e2e2e2;box-shadow:0 2px 10px rgba(0,0,0,.22);display:flex;flex-direction:column;align-items:center}
.service-icon{margin-top:50px;width:124px;height:124px;border-radius:50%;background:var(--teal)}
.service-name{margin-top:30px;text-align:center;color:var(--cyan);font-size:26px;font-weight:700;line-height:32px}

/* faq */
.faq{left:0;top:1895px;width:1200px;height:638px;background:linear-gradient(180deg,#0b2b2e 0%,#123436 40%,#2c3433 70%,#3d3027 100%)}
.faq-title{left:0;top:1928px;width:1200px;text-align:center;color:var(--white);font-size:50px}
.faq-item{position:absolute;left:173px;width:850px;border:2px solid var(--white);border-radius:6px;color:var(--white)}
.faq-q{display:flex;align-items:center;height:40px;padding-left:30px;font-size:15px;font-weight:700}
.faq-q span{width:20px}
.faq-a{padding:4px 220px 0 48px;font-size:15px;line-height:21px}

/* contact */
.contact{left:0;top:2533px;width:1200px;height:578px;background:var(--muted)}
.contact-title{left:0;top:2592px;width:1200px;text-align:center;font-size:48px;color:#111}
.field{position:absolute;background:var(--white);border:1px solid var(--line);border-radius:3px;font-size:13px;color:#333;padding:10px 14px;font-family:"Roboto",Arial,sans-serif}
.submit{left:531px;top:2987px;width:123px;height:42px;background:var(--teal);font-size:17px}

/* footer */
.footer{left:0;top:3111px;width:1200px;height:398px;background:var(--teal)}
.foot-head{position:absolute;top:3168px;color:var(--white);font-size:31px}
.foot-links{left:410px;top:3257px;list-style:none}
.foot-links li{font-size:16px;line-height:29px;color:var(--white)}
.foot-text{color:var(--white);font-size:16px;line-height:25px}
.news-input{left:603px;top:3326px;width:202px;height:36px;background:var(--white);border:1px solid #ccc;font-size:13px;padding:9px 8px}
.news-btn{left:608px;top:3382px;width:83px;height:34px;background:var(--white);color:#111;font-size:16px;font-weight:500}
.contact-line{position:absolute;left:871px;display:flex;gap:10px;color:var(--white);font-size:16px;line-height:23px;white-space:nowrap}
.contact-line svg{flex:none;margin-top:3px}
.copyright{left:92px;top:3454px;color:var(--white);font-size:16px}
.social{left:1030px;top:3457px;display:flex;gap:12px}
.social span{width:16px;height:16px;border-radius:50%;background:var(--white)}
</style>
</head>
<body>
<div class="page">

  <header class="hero">
    <svg class="hero-art" width="1200" height="720" viewBox="0 0 1200 720">
      <defs>
        <linearGradient id="heroSky" x1="0" y1="0" x2="0" y2="1">
          <stop offset="0" stop-color="#e8d7c3"/>
          <stop offset=".22" stop-color="#9ab8b0"/>
          <stop offset=".45" stop-color="#0f7d87"/>
          <stop offset=".62" stop-color="#0b7580"/>
          <stop offset=".9" stop-color="#18b4cc"/>
        </linearGradient>
        <linearGradient id="sessionTone" x1="0" y1="0" x2="1" y2="1">
          <stop offset="0" stop-color="#f2eee8"/>
          <stop offset=".4" stop-color="#c9a783"/>
          <stop offset=".7" stop-color="#8f8f86"/>
          <stop offset="1" stop-color="#3e4e66"/>
        </linearGradient>
        <clipPath id="heroClip"><rect x="0" y="0" width="1200" height="720"/></clipPath>
      </defs>
      <path d="M0 0H1200V560C1080 600 980 560 880 590C760 625 650 600 520 620C380 640 220 640 0 700Z" fill="url(#heroSky)"/>
      <g clip-path="url(#heroClip)" role="img" aria-label="Photo of a client talking with a therapist who holds a clipboard">
        <circle cx="978" cy="272" r="268" fill="url(#sessionTone)" stroke="#ffffff" stroke-width="3"/>
      </g>
    </svg>
    <div class="brand hero-brand">
      <div class="brand-dot"></div>
      <div class="brand-name">Brindle Oak</div>
    </div>
    <nav class="nav">
      <a href="#">Home</a><a href="#">About us</a><a href="#">Services</a><a href="#">FAQ</a><a href="#">Contact Us</a>
    </nav>
    <h1 class="hero-title script">Welcome to Brindle<br>Oak Wellness<br>Aftercare.</h1>
    <a class="btn hero-btn" href="#">View More</a>
  </header>

  <section class="about">
    <div class="abs about-frame"></div>
    <div class="abs about-photo" role="img" aria-label="Portrait photo of a smiling woman in front of green foliage"></div>
    <h2 class="abs about-title script">About us</h2>
    <p class="abs about-text">It is a long established fact that a reader will be distracted by the readable content of a page when looking at its layout. The point of using lorem ipsum is that it has a more-or-less normal distribution of letters.</p>
    <a class="btn about-btn" href="#">Read More</a>
  </section>

  <section class="services">
    <h2 class="abs services-title script">Services</h2>
    <div class="service-card" style="left:164px">
      <div class="service-icon" role="img" aria-label="Icon of a single person"></div>
      <div class="service-name">Individual<br>Psychotherapy</div>
    </div>
    <div class="service-card" style="left:471px">
      <div class="service-icon" role="img" aria-label="Icon of an eye"></div>
      <div class="service-name" style="margin-top:44px">EMDR</div>
    </div>
    <div class="service-card" style="left:781px">
      <div class="service-icon" role="img" aria-label="Icon of a family group"></div>
      <div class="service-name">Family<br>Therapy</div>
    </div>
  </section>

  <section>
    <div class="abs faq" role="img" aria-label="Dark photo of ocean waves on a sandy shore"></div>
    <h2 class="abs faq-title script">Faq</h2>
    <div class="faq-item" style="top:2044px;height:125px">
      <div class="faq-q"><span>–</span>The standard Lorem Ipsum passage, used since the 1500s</div>
      <p class="faq-a">Lorem ipsum dolor sit amet, consectetur adipiscing elit, sed do eiusmod tempor incididunt ut labore et dolore magna aliqua. Ut enim ad minim veniam, quis nostrud</p>
    </div>
    <div class="faq-item" style="top:2186px"><div class="faq-q"><span>+</span>Section 1.10.32 of "de Finibus Bonorum et Malorum", written by Cicero in 45 BC</div></div>
    <div class="faq-item" style="top:2245px"><div class="faq-q"><span>+</span>1914 translation by H. Rackham</div></div>
    <div class="faq-item" style="top:2305px"><div class="faq-q"><span>+</span>Section 1.10.33 of "de Finibus Bonorum et Malorum", written by Cicero in 45 BC</div></div>
    <div class="faq-item" style="top:2364px"><div class="faq-q"><span>+</span>1914 translation by H. Rackham</div></div>
    <div class="faq-item" style="top:2422px"><div class="faq-q"><span>+</span>What if the candidate provided leaves our employment?</div></div>
  </section>

  <section>
    <div class="abs contact"></div>
    <h2 class="abs contact-title script">Contact Us</h2>
    <div class="field" style="left:129px;top:2720px;width:458px;height:38px">Name</div>
    <div class="field" style="left:613px;top:2720px;width:457px;height:38px">Email</div>
    <div class="field" style="left:129px;top:2774px;width:458px;height:38px">Phone Number</div>
    <div class="field" style="left:613px;top:2774px;width:457px;height:38px">Appointments</div>
    <div class="field" style="left:129px;top:2828px;width:941px;height:113px">Messages</div>
    <a class="btn submit" href="#">Submit</a>
  </section>

  <footer>
    <div class="abs footer"></div>
    <div class="brand footer-brand">
      <div class="brand-dot"></div>
      <div class="brand-name">Brindle Oak</div>
    </div>
    <h3 class="foot-head script" style="left:410px">Quick Link</h3>
    <ul class="abs foot-links">
      <li>Home</li><li>About us</li><li>Services</li><li>FAQ</li><li>Contact Us</li>
    </ul>
    <h3 class="foot-head script" style="left:603px">Newsletter</h3>
    <p class="abs foot-text" style="left:603px;top:3258px;width:210px">Register your email for News for Brindle Oak</p>
    <div class="abs news-input">Enter the email</div>
    <a class="btn news-btn" href="#">Submit</a>
    <h3 class="foot-head script" style="left:877px">Contact us</h3>
    <div class="contact-line" style="top:3260px">
      <svg width="18" height="20" viewBox="0 0 18 20"><path d="M9 0C4.6 0 1.5 3.2 1.5 7.3 1.5 12 9 20 9 20s7.5-8 7.5-12.7C16.5 3.2 13.4 0 9 0zm0 10.2a3 3 0 1 1 0-6 3 3 0 0 1 0 6z" fill="#fff"/></svg>
      <span>412 Harbourline Ave, Unit 7<br>Seabrook, ON<br>K0L 2B9</span>
    </div>
    <div class="contact-line" style="top:3331px">
      <svg width="18" height="18" viewBox="0 0 24 24"><path d="M6.6 10.8a15.1 15.1 0 0 0 6.6 6.6l2.2-2.2c.3-.3.7-.4 1-.2 1.1.4 2.3.6 3.6.6.6 0 1 .4 1 1V20c0 .6-.4 1-1 1A17 17 0 0 1 3 4c0-.6.4-1 1-1h3.5c.6 0 1 .4 1 1 0 1.3.2 2.5.6 3.6.1.3 0 .7-.2 1z" fill="#fff"/></svg>
      <span>555.013.4826 (BO12)</span>
    </div>
    <div class="contact-line" style="top:3375px">
      <svg width="18" height="14" viewBox="0 0 18 14"><rect x="1" y="1" width="16" height="12" fill="none" stroke="#fff" stroke-width="1.6"/><path d="M1 1l8 7 8-7" fill="none" stroke="#fff" stroke-width="1.6"/></svg>
      <span>hello@brindleoak.example</span>
    </div>
    <p class="abs copyright">Copyright © 2019 Brindle Oak All Rights Reserved.</p>
    <div class="abs social" aria-label="Social links"><span></span><span></span><span></span></div>
  </footer>

</div>
</body>
</html>
```